card design for engineering consultancy

engineering drafting and project management company the provides drafting services for.
Electrical, Hydraulic, Mechanical, and Civil services
The company is called Q7R Services and logo is as attached
Information on card should be.
1. Logo
2.website : Q7RServices.example
3. email : info@Q7RServices.example
4. Phone: (+61) 400512836
5. Motto: Design - Document - Develop - Deliver

this card should be basically used for business identification only

Target Market(s)

electricians plumbers air conditioning installers and civil contractors

Industry/Entity Type

engineering, drafting, electrical, plumbing, airconditioning, civil

Contact Information for Business Card

1. Logo 2.website : Q7RServices.example 3. email : info@Q7RServices.example 4. Phone: (+61) 400512836 5. Motto: Design - Document - Develop - Deliver

Font styles to use
Serif

Requirements
Must have
• logo
Nice to have
• something inovative and different that makes it stand out from being just another business card

```html
<!DOCTYPE html>
<html lang="en">
<head>
<meta charset="UTF-8">
<title>Q7R Services – Business Card</title>
<link rel="stylesheet" href="https://fonts.googleapis.com/css2?family=Michroma&family=Barlow:wght@500;600&family=Roboto:wght@400&display=swap">
<style>
  :root {
    --stage: #1d1d1f;
    --card-black: #141414;
    --card-black-light: #2a2a2c;
    --card-white: #ffffff;
    --ink: #1b1b1b;
    --accent-red: #e01b22;
    --name-white: #f3efe6;
    --band-black: #151515;
  }
  * { box-sizing: border-box; margin: 0; padding: 0; }
  html, body { width: 1200px; height: 800px; overflow: hidden; }
  body {
    background: var(--stage);
    position: relative;
    font-family: "Roboto", sans-serif;
  }
  .card {
    position: absolute;
    left: 340px;
    width: 520px;
    height: 290px;
    border-radius: 16px;
    overflow: hidden;
  }
  .card--front {
    top: 95px;
    background: radial-gradient(ellipse at 50% 45%, var(--card-black-light) 0%, var(--card-black) 75%);
    display: flex;
    align-items: center;
    justify-content: center;
  }
  .brand {
    display: flex;
    align-items: center;
    gap: 16px;
  }
  .brand__square {
    width: 22px;
    height: 22px;
    background: var(--accent-red);
  }
  .brand__name {
    font-family: "Michroma", sans-serif;
    font-size: 26px;
    letter-spacing: 2px;
    color: var(--name-white);
    text-transform: uppercase;
  }
  .card--back {
    top: 415px;
    background: var(--card-white);
  }
  .back__tab {
    position: absolute;
    left: 30px;
    top: 0;
    width: 26px;
    height: 112px;
    background: var(--accent-red);
    border-radius: 0 0 13px 13px;
    display: flex;
    align-items: flex-end;
    justify-content: center;
    padding-bottom: 8px;
  }
  .motto {
    position: absolute;
    left: 70px;
    top: 58px;
    font-family: "Barlow", sans-serif;
    font-weight: 600;
    font-size: 19px;
    line-height: 22px;
    color: var(--ink);
    text-transform: uppercase;
  }
  .motto .hl { color: var(--accent-red); }
  .contacts {
    position: absolute;
    left: 36px;
    top: 160px;
    list-style: none;
  }
  .contacts li {
    display: flex;
    align-items: center;
    gap: 18px;
    height: 26px;
    font-size: 16px;
    color: var(--ink);
  }
  .contacts svg { width: 15px; height: 15px; fill: var(--accent-red); }
  .back__band {
    position: absolute;
    top: 0;
    right: 0;
    width: 150px;
    height: 100%;
    background: var(--band-black);
    clip-path: polygon(18% 0, 100% 0, 100% 100%, 0 100%);
  }
</style>
</head>
<body>
  <section class="card card--front">
    <div class="brand">
      <span class="brand__square"></span>
      <span class="brand__name">Q7R Services</span>
    </div>
  </section>

  <section class="card card--back">
    <div class="back__tab">
      <svg width="14" height="14" viewBox="0 0 24 24" fill="#fff" aria-hidden="true">
        <circle cx="12" cy="7" r="5"/><path d="M2 23c0-6 4.5-9 10-9s10 3 10 9z"/>
      </svg>
    </div>
    <p class="motto">
      Design-<span class="hl">Document</span><br>
      <span class="hl">Develop</span>-Deliver
    </p>
    <ul class="contacts">
      <li>
        <svg viewBox="0 0 24 24" aria-hidden="true"><path d="M6.6 10.8a15.5 15.5 0 0 0 6.6 6.6l2.2-2.2c.3-.3.7-.4 1-.2 1.1.4 2.3.6 3.6.6.6 0 1 .4 1 1V20c0 .6-.4 1-1 1A17 17 0 0 1 3 4c0-.6.4-1 1-1h3.5c.6 0 1 .4 1 1 0 1.3.2 2.5.6 3.6.1.3 0 .7-.2 1z"/></svg>
        (+61) 400512836
      </li>
      <li>
        <svg viewBox="0 0 24 24" aria-hidden="true"><path d="M12 2a7 7 0 0 0-7 7c0 5.2 7 13 7 13s7-7.8 7-13a7 7 0 0 0-7-7zm0 9.5A2.5 2.5 0 1 1 12 6.5a2.5 2.5 0 0 1 0 5z"/></svg>
        Q7RServices.example
      </li>
      <li>
        <svg viewBox="0 0 24 24" aria-hidden="true"><path d="M2 5h20v2l-10 6L2 7z"/><path d="M2 9.3l10 6 10-6V19H2z"/></svg>
        info@Q7RServices.example
      </li>
    </ul>
    <div class="back__band"></div>
  </section>
</body>
</html>
```